Stylish yet Funky Poster

We are a hair and beauty salon and have won some awards recently that we would like to display winning images in our window fronts.
Our windows are 900mm wide, 2100mm high. We have high res images and need to add some text somewhere on the image.
Salon colours are green, white though perhaps using black would be OK too.
I would like the text to read:-
2010 National Velora Shade Award Winner
2010 Qld Velora Shade Award Winner
(text as large as possible)

Model by Tom Pelling - (this text can be smaller)

The image is important but the more important purpose of the poster is to let passers by know about the competition wins.
Updates

Hi I've uploaded a new Dravik Logo which should be more clear.

I have uploaded bauhaus font also

Target Market(s)

Our target market are ladies 25 - 55 years old, mostly professional women.

Industry/Entity Type

Beauty Salon

Requirements
Must have
• Be 900mm wide, 2100mm high
• Must include supplied image.
• Must include text: 2010 National Velora Shade Award Winner,
• 2010 Qld Velora Shade Award Winner
• Model by Tom Pelling
Nice to have
• Salon name - Cobalt Hair & Beauty
• We also won 2008 National Velora Shade Award too - this may be used on same banner
• Background can be changed
• Either black or white version of Dravik logo attached

```html
<!DOCTYPE html>
<html lang="en">
<head>
<meta charset="utf-8">
<title>Cobalt Hair &amp; Beauty – Velora Shade Award Winner 2010</title>
<link rel="stylesheet" href="https://fonts.googleapis.com/css2?family=Montserrat:wght@400;500;700&display=swap">
<style>
  :root {
    --paper: #ffffff;
    --salon-green: #5aa83e;
    --band-green: rgba(86, 168, 58, 0.92);
    --band-grey: rgba(100, 100, 100, 0.86);
    --ink: #111111;
    --text-light: #ffffff;
    --hair: #7a1a2e;
    --hair-light: #a3283f;
    --skin: #e8c6b4;
    --dress: #151515;
  }
  html, body {
    margin: 0;
    padding: 0;
    overflow: hidden;
    background: var(--paper);
  }
  .poster {
    position: relative;
    width: 841px;
    height: 1200px;
    overflow: hidden;
    background: var(--paper);
    font-family: "Montserrat", sans-serif;
    color: var(--text-light);
  }
  .model-photo {
    position: absolute;
    inset: 0;
    background:
      radial-gradient(ellipse 230px 260px at 440px 290px, var(--hair-light) 0%, var(--hair) 70%, rgba(122,26,46,0) 100%),
      radial-gradient(ellipse 170px 260px at 450px 520px, var(--skin) 0%, var(--skin) 65%, rgba(232,198,180,0) 100%),
      radial-gradient(ellipse 420px 520px at 430px 1080px, var(--dress) 0%, var(--dress) 70%, rgba(21,21,21,0) 100%),
      radial-gradient(ellipse 420px 260px at 330px 820px, var(--skin) 0%, rgba(232,198,180,0) 100%),
      linear-gradient(180deg, #fbfbfb 0%, #f2f2f2 100%);
  }
  .salon-mark {
    position: absolute;
    left: 84px;
    top: 112px;
    display: flex;
    align-items: center;
    gap: 8px;
    color: var(--salon-green);
    font-weight: 500;
    line-height: 1.05;
  }
  .salon-mark .dot {
    width: 14px;
    height: 14px;
    border-radius: 50%;
    background: var(--salon-green);
  }
  .salon-mark .name { font-size: 30px; }
  .salon-mark .sub { font-size: 11px; }
  .partner-mark {
    position: absolute;
    left: 622px;
    top: 652px;
    width: 168px;
    height: 78px;
    background: var(--paper);
    display: flex;
    align-items: center;
    justify-content: center;
    color: var(--ink);
    font-weight: 400;
    font-size: 40px;
    letter-spacing: 1px;
  }
  .award-band {
    position: absolute;
    display: flex;
    align-items: center;
    box-sizing: border-box;
    margin: 0;
  }
  .award-band .year {
    font-weight: 700;
    font-size: 104px;
    letter-spacing: -2px;
    line-height: 1;
  }
  .award-band .title {
    margin: 0;
    line-height: 1;
  }
  .award-band .title .event { display: block; font-weight: 400; font-size: 38px; }
  .award-band .title .prize { display: block; font-weight: 700; font-size: 50px; margin-top: 2px; }
  .award-band--national {
    left: 40px;
    top: 808px;
    width: 745px;
    height: 122px;
    background: var(--band-grey);
    padding-left: 14px;
    gap: 22px;
  }
  .award-band--state {
    left: 52px;
    top: 952px;
    width: 789px;
    height: 123px;
    background: var(--band-green);
    padding-left: 40px;
    gap: 34px;
  }
  .award-band--state .title .event { font-size: 38px; }
  .award-band--state .title .prize { font-size: 46px; }
  .credit {
    position: absolute;
    right: 24px;
    bottom: 14px;
    margin: 0;
    display: flex;
    align-items: center;
    gap: 8px;
    font-size: 19px;
    font-weight: 400;
  }
  .credit .dot {
    width: 12px;
    height: 12px;
    border: 2px solid var(--text-light);
    border-radius: 50%;
  }
</style>
</head>
<body>
  <main class="poster">
    <div class="model-photo" role="img" aria-label="Salon photograph on a white backdrop: model with a glossy burgundy-red angled bob wearing a black halter dress with fabric flowers"></div>

    <div class="salon-mark">
      <span class="dot"></span>
      <div>
        <div class="name">Cobalt</div>
        <div class="sub">Hair &amp; Beauty</div>
      </div>
    </div>

    <div class="partner-mark">Dravik</div>

    <section class="award-band award-band--national">
      <span class="year">2010</span>
      <h2 class="title">
        <span class="event">National Velora Shade</span>
        <span class="prize">Award Winner</span>
      </h2>
    </section>

    <section class="award-band award-band--state">
      <h2 class="title">
        <span class="event">Qld Velora Shade</span>
        <span class="prize">Award Winner</span>
      </h2>
      <span class="year">2010</span>
    </section>

    <p class="credit"><span class="dot"></span>Model by Tom Pelling</p>
  </main>
</body>
</html>
```